Looking for something outstanding

2 side business card, one side just the logo preferably the metallic 3D color or my original logo for uv printing. Be creative

Colors

Designer to choose colors to be used in the design.

Requirements
Must have
• Here my info for the business cards
• Marco Delgado
• President
• (214) 555-0173
• Marco@crestlinebuilders.com
• Office@crestlinebuilders.com
• www.crestlinebuilders.com
• FB @crestlinebuilders
• Dallas-Fort Worth

```html
<!DOCTYPE html>
<html lang="en">
<head>
<meta charset="utf-8">
<title>Crestline Builders – Business Card</title>
<link href="https://fonts.googleapis.com/css2?family=Montserrat:wght@400;500;600&display=swap" rel="stylesheet">
<style>
  :root {
    --stage: #3a3a3a;
    --stage-dark: #1c1c1c;
    --card: #1f1f20;
    --card-edge: #141414;
    --logo-emboss: #3b3b3d;
    --red: #e02a2a;
    --blue: #3d55c4;
    --ink: #e9e9ea;
  }
  * { box-sizing: border-box; margin: 0; padding: 0; }
  html, body { width: 1200px; height: 960px; overflow: hidden; }
  body {
    background: radial-gradient(ellipse at 50% 40%, var(--stage) 0%, var(--stage-dark) 100%);
    font-family: "Montserrat", sans-serif;
    position: relative;
  }
  .card {
    position: absolute;
    width: 700px;
    height: 400px;
    background: var(--card);
    border-radius: 22px;
    box-shadow: 0 6px 0 var(--card-edge), 0 24px 40px rgba(0,0,0,.55);
    overflow: hidden;
  }
  .card--front { left: 70px; top: 50px; }
  .card--back  { left: 430px; top: 500px; }

  /* front: logo only, UV-gloss wordmark */
  .front-logo {
    position: absolute; inset: 0;
    display: flex; align-items: center; justify-content: center; gap: 16px;
  }
  .front-logo__mark {
    width: 32px; height: 32px; border-radius: 50%;
    background: var(--logo-emboss); flex: none;
  }
  .front-logo__name {
    font-weight: 500; font-size: 38px; letter-spacing: 5px;
    color: var(--logo-emboss); text-transform: uppercase; white-space: nowrap;
  }

  /* back: contact side */
  .back-glow {
    position: absolute; right: -60px; top: -40px;
    width: 460px; height: 460px; border-radius: 50%;
    background: radial-gradient(circle, rgba(255,255,255,.04) 0%, rgba(255,255,255,0) 70%);
  }
  .back-content { position: absolute; left: 48px; top: 38px; }
  .brand { display: flex; align-items: center; gap: 12px; margin-bottom: 22px; }
  .brand__dot { width: 22px; height: 22px; background: var(--red); }
  .brand__name {
    font-weight: 600; font-size: 28px; letter-spacing: 3px;
    color: var(--red); text-transform: uppercase;
  }
  .person__name { font-size: 30px; font-weight: 500; text-transform: uppercase; letter-spacing: 1px; line-height: 1.2; }
  .person__first { color: var(--red); }
  .person__last { color: var(--blue); }
  .person__title { color: var(--ink); font-size: 19px; margin-top: 2px; }
  .divider { width: 62px; height: 2px; background: var(--red); margin: 12px 0 12px; }
  .contact { list-style: none; }
  .contact li {
    display: flex; align-items: center; gap: 12px;
    color: var(--ink); font-size: 16px; line-height: 26px;
  }
  .contact svg { width: 15px; height: 15px; flex: none; }
  .accent { color: var(--red); }
</style>
</head>
<body>

  <section class="card card--front" aria-label="Business card front">
    <div class="front-logo">
      <span class="front-logo__mark"></span>
      <span class="front-logo__name">Crestline Builders</span>
    </div>
  </section>

  <section class="card card--back" aria-label="Business card back">
    <div class="back-glow"></div>
    <div class="back-content">
      <div class="brand">
        <span class="brand__dot"></span>
        <span class="brand__name">Crestline Builders</span>
      </div>
      <h1 class="person__name"><span class="person__first">Marco</span> <span class="person__last">Delgado</span></h1>
      <p class="person__title">President</p>
      <div class="divider"></div>
      <ul class="contact">
        <li>
          <svg viewBox="0 0 16 16" aria-hidden="true"><path fill="#e02a2a" d="M8 1a5 5 0 0 0-5 5c0 3.8 5 9 5 9s5-5.2 5-9a5 5 0 0 0-5-5zm0 7a2 2 0 1 1 0-4 2 2 0 0 1 0 4z"/></svg>
          Dallas-Fort Worth
        </li>
        <li>
          <svg viewBox="0 0 16 16" aria-hidden="true"><path fill="#e02a2a" d="M4 1.5l2.2 3-1.3 1.4c.8 1.8 2.2 3.2 4 4l1.4-1.3 3 2.2-1.2 2.4C6.6 13.4 2.6 9.4 1.6 3.7z"/></svg>
          (214) 555-0173
        </li>
        <li>
          <svg viewBox="0 0 16 16" aria-hidden="true"><rect x="1" y="3" width="14" height="10" fill="#e02a2a"/><path d="M1 3l7 6 7-6" fill="none" stroke="#1f1f20" stroke-width="1.4"/></svg>
          Marco@crestlinebuilders.com
        </li>
        <li>
          <svg viewBox="0 0 16 16" aria-hidden="true"><rect x="1" y="3" width="14" height="10" fill="#e02a2a"/><path d="M1 3l7 6 7-6" fill="none" stroke="#1f1f20" stroke-width="1.4"/></svg>
          Office@crestlinebuilders.com
        </li>
        <li>
          <svg viewBox="0 0 16 16" aria-hidden="true"><circle cx="8" cy="8" r="6.5" fill="none" stroke="#e02a2a" stroke-width="1.6"/><path d="M1.5 8h13M8 1.5c-3 3.5-3 9.5 0 13M8 1.5c3 3.5 3 9.5 0 13" fill="none" stroke="#e02a2a" stroke-width="1.2"/></svg>
          <span>www.<span class="accent">crestlinebuilders</span>.com</span>
        </li>
        <li>
          <svg viewBox="0 0 16 16" aria-hidden="true"><circle cx="8" cy="8" r="6" fill="#e02a2a"/></svg>
          FB @crestlinebuilders
        </li>
      </ul>
    </div>
  </section>

</body>
</html>
```